Web App Dashboard Design for a HOMEPULSE

We are a company that gives consultancy and installation services for custom HOMEPULSE designs to household owners in ON, Canada. For our web application, we are in need of a dashboard design which will display multiple rooms that could be present in a home. This should be a flexible design as the number of rooms where smart devices installed will vary from house to house. We would like to see the name of the rooms and several icons that represent different monitored objects in each room like temperature, light on/off, sound/music on/off, humidity, illuminance, noise level, air quality, for bathrooms and kitchens wet/dry conditions, windows/doors open, curtains open/closed etc. The web application will collect the latest status data from all related sensors and it will be publishing the latest status for each room into this dashboard. Backend of the dashboards should contain nice modern looking houses and it would be good if there are multiple versions of the background pictures that rotate.

Target Market(s)

Mid-Market range house holders who want to increase their comfort and safety with HOMEPULSE implementations

Industry/Entity Type

Small Business

Number of Pages Required

1 page

Colors
0455a3
3277b5
85acd3
86cae7
fbf289
cadf82
acd037
9bcb3c
faa54b

Requirements
Must have
• - A Flexible Dashboard Design which can hold many rooms but still look sharp even with only 1/2 rooms as well.
• - An HOMEPULSE icon library that will show the monitored value like temperature, lights on/off, door/window open/close etc.

```html
<!DOCTYPE html>
<html lang="en">
<head>
<meta charset="utf-8">
<title>HomePulse Dashboard</title>
<link rel="stylesheet" href="https://fonts.googleapis.com/css2?family=Poppins:wght@400;500;600&display=swap">
<style>
:root{
  --brand-blue:#0455a3;
  --title-blue:#1d5ba8;
  --header-top:#3f73b0;
  --header-bottom:#2a5ea4;
  --accent:#f47a1f;
  --accent-light:#f7923a;
  --page-bg:#eef2f8;
  --card-bg:#f3f5f9;
  --card-border:#b9bec6;
  --nav-grey:#cfcfcf;
  --nav-text:#9a9a9a;
  --text-dark:#222;
}
*{box-sizing:border-box;margin:0;padding:0}
html,body{width:1200px;height:1088px;overflow:hidden;background:#fff;font-family:'Poppins',sans-serif}
.app{position:relative;width:1200px;height:1088px}
.sidebar{position:absolute;left:0;top:0;width:186px;height:1088px;background:#fff}
.brand{height:141px;display:flex;flex-direction:column;align-items:center;justify-content:center;gap:8px}
.brand-mark{width:22px;height:22px;background:var(--accent);border-radius:50%}
.brand-name{font-weight:600;font-size:21px;color:var(--brand-blue);letter-spacing:.3px}
.nav{list-style:none}
.nav-item{height:52px;display:flex;align-items:center;justify-content:space-between;padding:0 30px 0 31px;font-size:16px;color:var(--nav-text)}
.nav-item:nth-child(odd){background:var(--nav-grey);color:#a8a8a8}
.nav-item:nth-child(even){background:#fff}
.nav-item.active{background:linear-gradient(90deg,#f37021,#f7923a);color:#fff;height:51px}
.nav-item svg{width:24px;height:24px;fill:none;stroke:currentColor;stroke-width:1.3;opacity:.8}
.nav-item.active svg{opacity:1;stroke-width:1.8}
.topbar{position:absolute;left:186px;top:0;width:1014px;height:74px;background:linear-gradient(180deg,var(--header-top),var(--header-bottom));display:flex;align-items:center;padding:0 50px 0 35px;color:#fff}
.search{display:flex;align-items:center;gap:9px;font-size:12px;flex:1}
.search svg{width:16px;height:16px;stroke:#fff;stroke-width:2.6;fill:none}
.top-icons{display:flex;align-items:center;gap:28px}
.top-icons svg{fill:none;stroke:#fff;stroke-width:1.3}
.avatar{width:33px;height:33px;border-radius:50%;background:#b88a6a;border:2px solid #fff}
.user{font-size:11.5px;font-weight:500;display:flex;align-items:center;gap:3px;margin-left:-10px}
.content{position:absolute;left:186px;top:74px;width:1014px;height:525px;background:var(--page-bg)}
.grid{position:absolute;left:43px;top:28px;display:grid;grid-template-columns:repeat(4,216px);grid-auto-rows:140px;column-gap:21px;row-gap:22px}
.card{background:var(--card-bg);border:1px solid var(--card-border);display:flex;flex-direction:column;align-items:center;padding-top:24px}
.reading{height:60px;display:flex;align-items:flex-end;gap:6px;color:var(--accent)}
.reading svg{fill:none;stroke:var(--accent);stroke-width:2}
.value{font-size:16px;font-weight:500;margin-bottom:6px}
.toggle{width:75px;height:29px;border-radius:15px;background:var(--accent);display:flex;align-items:center;justify-content:space-between;padding:0 3px 0 9px;color:#fff;font-size:16px;font-weight:500;margin-bottom:10px}
.toggle::after{content:"";width:23px;height:23px;border-radius:50%;background:#fff}
.toggle.wide{width:88px}
.room-title{margin-top:12px;font-size:19.5px;font-weight:600;color:var(--title-blue)}
.floorplan{position:absolute;left:186px;top:599px;width:1014px;height:435px;background:radial-gradient(ellipse at 50% 50%,#b9b4ab 0%,#c9c6c1 45%,#d7d7d7 80%)}
.footer{position:absolute;left:186px;top:1034px;width:1014px;height:54px;display:flex;align-items:center;justify-content:center;font-size:17px;color:var(--text-dark)}
</style>
</head>
<body>
<div class="app">
  <aside class="sidebar">
    <div class="brand"><span class="brand-mark"></span><span class="brand-name">HOMEPULSE</span></div>
    <ul class="nav">
      <li class="nav-item active">Dashboard<svg viewBox="0 0 24 24"><path d="M4 18a9 9 0 1 1 16 0"/><path d="M12 14l5-6"/></svg></li>
      <li class="nav-item">Invoice<svg viewBox="0 0 24 24"><rect x="6" y="3" width="13" height="18"/><path d="M9 9l2 2 4-4M9 15h7"/></svg></li>
      <li class="nav-item">My tasks<svg viewBox="0 0 24 24"><rect x="5" y="3" width="14" height="18"/><path d="M8 8h8M8 12h8M8 16h8"/></svg></li>
      <li class="nav-item">Reports<svg viewBox="0 0 24 24"><path d="M4 21h16M6 20v-3M10 20v-5M14 20v-8M18 20V6"/></svg></li>
      <li class="nav-item">Settings<svg viewBox="0 0 24 24"><circle cx="12" cy="12" r="3"/><circle cx="12" cy="12" r="8" stroke-dasharray="4 2"/></svg></li>
      <li class="nav-item">Support<svg viewBox="0 0 24 24"><circle cx="12" cy="9" r="4"/><path d="M5 21c1-5 13-5 14 0M7 9a5 5 0 0 1 10 0"/></svg></li>
      <li class="nav-item">FAQ<svg viewBox="0 0 24 24"><rect x="4" y="4" width="10" height="9"/><rect x="10" y="10" width="10" height="9"/></svg></li>
    </ul>
  </aside>

  <header class="topbar">
    <div class="search"><svg viewBox="0 0 16 16"><circle cx="6.5" cy="6.5" r="4.8"/><path d="M10 10l4.5 4.5"/></svg>Type in to search...</div>
    <div class="top-icons">
      <svg width="26" height="18" viewBox="0 0 26 18"><rect x="1" y="1" width="24" height="16"/><path d="M1 1l12 9 12-9"/></svg>
      <svg width="18" height="20" viewBox="0 0 18 20"><path d="M4 15V9a5 5 0 0 1 10 0v6l2 2H2z"/><circle cx="14" cy="5" r="2" fill="#fff"/></svg>
      <div class="avatar" role="img" aria-label="User profile photo"></div>
      <div class="user">Daniel Reyes <svg width="8" height="6" viewBox="0 0 8 6"><path d="M1 1l3 3 3-3"/></svg></div>
    </div>
  </header>

  <main class="content">
    <div class="grid">
      <div class="card"><div class="reading"><svg width="26" height="52" viewBox="0 0 26 52"><path d="M9 4a4 4 0 0 1 8 0v30a8 8 0 1 1-8 0z"/><circle cx="13" cy="41" r="3"/><path d="M13 14v24"/></svg><span class="value">60°C</span></div><div class="room-title">TEMPERATURE</div></div>
      <div class="card"><div class="reading"><svg width="50" height="52" viewBox="0 0 50 52"><path d="M18 38a11 11 0 1 1 14 0v6H18z"/><path d="M19 48h12M25 2v6M8 10l4 4M42 10l-4 4M2 26h6M42 26h6"/></svg><span class="toggle">On</span></div><div class="room-title">LIGHT</div></div>
      <div class="card"><div class="reading"><svg width="58" height="52" viewBox="0 0 58 52"><path d="M3 18h10l16-13v42L13 34H3z"/><path d="M36 16a13 13 0 0 1 0 20M42 9a22 22 0 0 1 0 34"/></svg><span class="toggle">On</span></div><div class="room-title">SOUND/MUSIC</div></div>
      <div class="card"><div class="reading"><svg width="42" height="52" viewBox="0 0 42 52"><path d="M20 3C12 17 5 25 5 34a15 15 0 0 0 30 0C35 25 28 17 20 3z"/><path d="M26 40l2 2M34 44l3-3"/></svg><span class="value">60%</span></div><div class="room-title">HUMIDITY</div></div>

      <div class="card"><div class="reading"><svg width="54" height="54" viewBox="0 0 54 54"><circle cx="27" cy="27" r="11"/><path d="M27 3v7M27 44v7M3 27h7M44 27h7M10 10l5 5M39 39l5 5M44 10l-5 5M10 44l5-5"/></svg><span class="value">60°C</span></div><div class="room-title">ILLUMINANCE</div></div>
      <div class="card"><div class="reading"><svg width="58" height="52" viewBox="0 0 58 52"><path d="M3 18h10l16-13v42L13 34H3z"/><path d="M36 16a13 13 0 0 1 0 20M42 9a22 22 0 0 1 0 34"/></svg><span class="value">80%</span></div><div class="room-title">NOISE LEVEL</div></div>
      <div class="card"><div class="reading"><svg width="76" height="54" viewBox="0 0 76 54"><rect x="2" y="2" width="72" height="26"/><path d="M2 20h72M28 36c-3 4 3 6 0 12M38 36c-3 4 3 6 0 12M48 36c-3 4 3 6 0 12"/></svg><span class="value">12°c</span></div><div class="room-title">AIR QUALITY</div></div>
      <div class="card"><div class="reading"><svg width="58" height="54" viewBox="0 0 58 54"><path d="M2 30h54M6 30v8a8 8 0 0 0 8 8h30a8 8 0 0 0 8-8v-8M12 46l-3 5M46 46l3 5M46 30V8a5 5 0 0 1 10 0"/><circle cx="16" cy="24" r="4"/></svg><span class="toggle">wet</span></div><div class="room-title">BATHROOMS</div></div>

      <div class="card"><div class="reading"><svg width="54" height="52" viewBox="0 0 54 52"><rect x="2" y="4" width="14" height="10"/><rect x="38" y="4" width="14" height="10"/><path d="M20 14l4-10h6l4 10z"/><rect x="2" y="24" width="50" height="26"/><path d="M2 34h50M18 24v26M36 24v26"/></svg><span class="toggle">wet</span></div><div class="room-title">KITCHENS</div></div>
      <div class="card"><div class="reading"><svg width="34" height="54" viewBox="0 0 34 54"><path d="M2 4h14v46H2z"/><path d="M16 4l14 4v42l-14 0z" fill="#f47a1f"/></svg><span class="toggle wide">Open</span></div><div class="room-title">WINDOWS/DOORS</div></div>
      <div class="card"><div class="reading"><svg width="62" height="54" viewBox="0 0 62 54"><path d="M2 2h58M4 4v48h54V4M4 4c6 12 10 24 12 48M58 4c-6 12-10 24-12 48M31 4v48M31 4c-6 12-6 30-6 48M31 4c6 12 6 30 6 48"/></svg><span class="toggle wide">Open</span></div><div class="room-title">CURTAINS</div></div>
    </div>
  </main>

  <div class="floorplan" role="img" aria-label="3D cutaway render of a modern apartment floor plan with kitchen, living room, bedrooms and terraces"></div>

  <footer class="footer">Copyrights © 2019. All right reserved.</footer>
</div>
</body>
</html>
```